STICKER DESIGN required for packaging. UK START UP TEA BUSINESS

We are looking for a design for a sticker that will be applied to packaging for our teas! We are a new start up Tea business based in the UK called 'BrookLeafs'
Selling quality loose leaf tea and teabags via our online shop and also face to face at farmers markets / food shows and eventually in our own tea emporium. We will be marketing our teas to hotels, cafes, delis etc. too
We carry every day teas eg. breakfast blends and also speciality and rare teas to offer customers the chance to try something new. Tea as a treat / ritual / indulgence / healthy lifestyle choice / modern
The design will initially be printed on vinyl stickers and then applied to the tea packaging (pouch bags in matte black and matte silver), in the future the design may be printed direct onto our packaging. The sticker design will need to be scalable as the size of the pouch bag varies dependant on the tea.
The sticker we have in mind is a leaf shape (sketch attached)
colour green to match our logo
It will include our logo (files attached)
Text to be included on the sticker is
- www.brookleafs.co.uk
- Welbury, England
- The tea type eg. Green
It will need to complement both black and silver pouches that we are using to package our teas (see attached image of our pouches)
Colours - green leaf, see our corporate colours (green & orange) on our logo files attached. We also like silver and black.
Font - nothing to swirly, must be easy to read on the packaging
once a sticker design is agreed for the initial tea type (Green) we will require additional files for each tea type that we stock. Just the tea type (Green) to be updated - the rest of the design to stay the same. The tea types we stock are listed below
Green
Black
Oolong
White
Herbal
Blended
Happy to answer any questions and aim to give feedback daily! Thank you for your interest

```html
<!DOCTYPE html>
<html lang="en">
<head>
<meta charset="utf-8">
<title>BrookLeafs – Green Tea Sticker</title>
<link href="https://fonts.googleapis.com/css2?family=Arimo:wght@400;700&family=Questrial&display=swap" rel="stylesheet">
<style>
  :root {
    --leaf-green: #a6d23e;
    --leaf-green-deep: #8cbd2c;
    --leaf-green-soft: #b4db55;
    --brand-orange: #f39a1e;
    --ink: #000000;
    --paper: #ffffff;
  }
  html, body {
    margin: 0;
    padding: 0;
    width: 900px;
    height: 1200px;
    overflow: hidden;
    background: var(--paper);
  }
  .presentation {
    display: block;
    width: 900px;
    height: 1200px;
  }
  .stage-dark { fill: var(--ink); }
  .stage-light { fill: var(--paper); }
  .leaf-band { fill: url(#band-pattern-fill); }
  .leaf-heart { fill: var(--ink); }
  .leaf-stem { fill: none; stroke: var(--leaf-green); stroke-width: 9; stroke-linecap: butt; }
  .band-text {
    font-family: "Arimo", Arial, sans-serif;
    font-weight: 700;
    font-size: 11.5px;
    letter-spacing: 0.8px;
    fill: var(--ink);
  }
  .brand-mark { fill: var(--brand-orange); }
  .brand-name {
    font-family: "Arimo", Arial, sans-serif;
    font-weight: 400;
    font-size: 29px;
    fill: var(--brand-orange);
  }
  .tagline {
    font-family: "Arimo", Arial, sans-serif;
    font-weight: 700;
    font-size: 10.5px;
    letter-spacing: 0.5px;
    fill: var(--leaf-green);
  }
  .rule { stroke: var(--brand-orange); stroke-width: 1.2; }
  .tea-type {
    font-family: "Questrial", "Arimo", sans-serif;
    font-size: 26px;
    fill: var(--leaf-green);
  }
</style>
</head>
<body>
<svg class="presentation" viewBox="0 0 900 1200" xmlns="http://www.w3.org/2000/svg" xmlns:xlink="http://www.w3.org/1999/xlink">
  <defs>
    <linearGradient id="band-pattern-fill" x1="0" y1="0" x2="1" y2="1">
      <stop offset="0" stop-color="var(--leaf-green-soft)"/>
      <stop offset="0.5" stop-color="var(--leaf-green)"/>
      <stop offset="1" stop-color="var(--leaf-green-deep)"/>
    </linearGradient>
    <path id="url-path" d="M347,302 C355,232 402,172 428,105"/>
    <path id="place-path" d="M442,438 C492,412 540,368 557,300"/>
    <g id="tea-sticker">
      <path class="leaf-stem" d="M410,456 C395,485 372,505 345,525"/>
      <path class="leaf-band" role="img" aria-label="Small leaf pattern along the green border" d="M430,55 C470,112 572,180 572,265 C572,362 492,440 410,462 C360,422 330,382 330,320 C330,230 402,160 430,55 Z"/>
      <path class="leaf-heart" d="M438,95 C458,132 546,200 546,270 C546,350 480,412 418,446 C375,416 355,376 355,320 C355,240 420,170 438,95 Z"/>

      <text class="band-text"><textPath xlink:href="#url-path" startOffset="4">www.brookleafs.co.uk</textPath></text>
      <text class="band-text"><textPath xlink:href="#place-path" startOffset="4">Welbury, England</textPath></text>

      <circle class="brand-mark" cx="462" cy="222" r="24"/>
      <text class="brand-name" x="456" y="285" text-anchor="middle">BrookLeafs</text>
      <text class="tagline" x="454" y="311" text-anchor="middle">Leaf Tea and Infusions</text>

      <line class="rule" x1="375" y1="328" x2="510" y2="328"/>
      <text class="tea-type" x="441" y="354" text-anchor="middle">green tea</text>
      <line class="rule" x1="375" y1="362" x2="510" y2="362"/>
    </g>
  </defs>

  <rect class="stage-dark" x="0" y="0" width="900" height="600"/>
  <rect class="stage-light" x="0" y="600" width="900" height="600"/>

  <use xlink:href="#tea-sticker"/>
  <use xlink:href="#tea-sticker" transform="translate(0,605)"/>
</svg>
</body>
</html>
```